Runners Report - 2 page freshen up from previous design

We need a report design to display information for runners in an easy to read - almost like an infographic format. Our software collect data on someones running style and gives us information based on this in the form of numbers. We then compare it to a database and display it back in a range of low, ideal, or, excessive. The purpose of the report is to give to the client after their running gait analysis assessment to help them better to understand their results ( which are currently very complicated). I would like to see the final design with simliar formats of the biomechanical man pictures ( currently i've used different ones for examples). I have shown an example of what im looking for, and i basically need it tidied up and made to look more professional. Our colours are navy blue, red, and white. I would be happy to see some options with a white background as well.

Needed:
2 page report:
First page is the running gait analysis information
Second page is strength flexibiltiy, structural and functional information
Data needs to be inputted and changed in these files everytime
I want it to look professional, but also a bit flashy ( or 'cool') and easy to read.

Target Market(s)

Runners , Triathletes, Sports people

Industry/Entity Type

Health And Wellness

Font styles to use
Serif
Sans Serif

Colors
0455a3
ec1f27
ffffff

Requirements
Must have
• All of the information I've given in my example.
• Must have a graph format with traffic light system for the parameters with Pelvis/hip/knee/ankle.
• Must have biomechanical men - 3D men running etc all in the same format/ design
• Must be able to input different data each time to change the results
• Must have Movik2 logo
Nice to have
• Different options - dark blue or white background?
Should not have
• cartoons or unrealistic figures

```html
<!DOCTYPE html>
<html lang="en">
<head>
<meta charset="utf-8">
<title>Runners Report</title>
<link rel="stylesheet" href="https://fonts.googleapis.com/css2?family=Montserrat:wght@400;500;600;700;800&display=swap">
<style>
:root{
  --navy-deep:#060d24;
  --navy:#0a1f55;
  --brand-blue:#0455a3;
  --glow:#3f78d6;
  --panel:rgba(58,64,86,.62);
  --panel-light:rgba(70,96,160,.45);
  --white:#ffffff;
  --red:#d71f26;
  --orange:#f08a12;
  --yellow:#f5d000;
  --green:#1c9a3a;
  --green-dark:#0d4d1c;
}
*{margin:0;padding:0;box-sizing:border-box}
html,body{width:849px;height:1200px;overflow:hidden;background:var(--navy-deep)}
body{font-family:"Montserrat",Arial,sans-serif;color:var(--white)}
.report{position:relative;width:849px;height:1200px;overflow:hidden;
  background:radial-gradient(ellipse at 60% 45%,#1d4fa8 0%,var(--navy) 45%,var(--navy-deep) 100%)}
.backdrop{position:absolute;inset:0;
  background:radial-gradient(ellipse 260px 520px at 340px 640px,rgba(120,170,255,.45),transparent 70%),
             radial-gradient(ellipse 200px 200px at 430px 540px,rgba(200,225,255,.5),transparent 70%)}
.panel{position:absolute;background:var(--panel)}
.panel.light{background:var(--panel-light)}
.panel-title{position:absolute;left:0;right:0;text-align:center;font-weight:600;font-size:13.5px;letter-spacing:1.6px}
.label{position:absolute;font-size:8.5px;font-weight:600;letter-spacing:.8px}
.rule{position:absolute;height:1px;background:var(--white)}

.header .title{position:absolute;left:0;right:0;top:40px;text-align:center;font-size:17px;font-weight:500;letter-spacing:2.4px}
.header .title-bar{position:absolute;left:352px;top:68px;width:30px;height:1.5px;background:var(--white)}
.brand{position:absolute;left:628px;top:26px;display:flex;align-items:center;gap:7px;font-weight:800;font-size:19px}
.brand-mark{width:10px;height:10px;border-radius:50%;background:var(--white)}

.artwork{position:absolute;left:50%;transform:translateX(-50%);background:radial-gradient(ellipse at center,#e9e4d8 0%,#bdb7a9 55%,transparent 75%)}

.meter{position:absolute;left:17px;right:17px;height:4px;
  background:linear-gradient(90deg,var(--red),var(--orange) 25%,var(--yellow) 50%,var(--green) 78%,var(--green-dark))}
.meter::after{content:"";position:absolute;left:var(--pos);top:-5px;width:5px;height:14px;margin-left:-2.5px;background:var(--white)}
.metric-name{position:absolute;left:0;right:0;text-align:center;font-size:11px;font-weight:600;letter-spacing:1px}
.metric-sub{position:absolute;left:0;right:0;text-align:center;font-size:7.5px;font-weight:600;letter-spacing:.9px}

.marker{position:absolute;width:5px;height:14px;background:var(--white)}
.big-number{position:absolute;font-weight:800;line-height:1}
.unit{position:absolute;font-size:8px;font-weight:600}
</style>
</head>
<body>
<main class="report">
  <div class="backdrop" role="img" aria-label="Blue network of glowing lines behind a translucent running figure"></div>

  <header class="panel header" style="left:42px;top:40px;width:760px;height:101px">
    <h1 class="title">RUNNERS REPORT</h1>
    <div class="title-bar"></div>
    <div class="brand"><span>Movik2</span><span class="brand-mark"></span></div>
  </header>

  <section class="panel" style="left:42px;top:150px;width:760px;height:60px">
    <span class="label" style="left:24px;top:20px;font-size:13px;letter-spacing:1.4px">RUNNERS NAME</span>
    <div class="rule" style="left:24px;right:30px;top:45px"></div>
  </section>

  <section class="panel" style="left:42px;top:222px;width:180px;height:143px">
    <span class="label" style="left:21px;top:20px;font-size:10.5px;letter-spacing:1.2px">RUNNER DETAILS</span>
    <span class="label" style="left:21px;top:55px">DOB</span>
    <div class="rule" style="left:21px;width:135px;top:70px"></div>
    <span class="label" style="left:21px;top:97px">WEGHT</span>
    <div class="rule" style="left:21px;width:135px;top:112px"></div>
  </section>

  <section class="panel light" style="left:235px;top:222px;width:567px;height:143px">
    <span class="label" style="left:22px;top:20px;font-size:10.5px;letter-spacing:1.2px">ANALYSIS DETAILS</span>
    <span class="label" style="left:22px;top:55px">DATE</span>
    <div class="rule" style="left:22px;width:254px;top:70px"></div>
    <span class="label" style="left:294px;top:55px">ORTHOTICS &nbsp;&nbsp; RUNNING/ WALKING</span>
    <div class="rule" style="left:294px;width:254px;top:70px"></div>
    <span class="label" style="left:22px;top:97px">SHOE</span>
    <div class="rule" style="left:22px;width:254px;top:112px"></div>
    <span class="label" style="left:294px;top:97px">SPEED</span>
    <div class="rule" style="left:294px;width:254px;top:112px"></div>
  </section>

  <!-- Joint panels -->
  <section class="panel light" style="left:42px;top:376px;width:181px;height:388px">
    <h2 class="panel-title" style="top:10px">PELVIS</h2>
    <div class="artwork" role="img" aria-label="Anatomical model of the pelvis" style="top:36px;width:140px;height:108px"></div>
    <div class="metric-name" style="top:182px">FRONTAL</div><div class="metric-sub" style="top:195px">COLLAPS</div>
    <div class="meter" style="top:213px;--pos:20%"></div>
    <div class="metric-name" style="top:252px">SAGITTAL</div><div class="metric-sub" style="top:265px">FORWARD TILT</div>
    <div class="meter" style="top:283px;--pos:63%"></div>
    <div class="metric-name" style="top:322px">TRANSVERS</div><div class="metric-sub" style="top:335px">ROTATION AT FOOTSTRIKE</div>
    <div class="meter" style="top:353px;--pos:27%"></div>
  </section>

  <section class="panel light" style="left:235px;top:376px;width:181px;height:388px">
    <h2 class="panel-title" style="top:10px">HIP</h2>
    <div class="artwork" role="img" aria-label="Anatomical model of the hip joints" style="top:36px;width:135px;height:108px"></div>
    <div class="metric-name" style="top:182px">FRONTAL</div><div class="metric-sub" style="top:195px">COLLAPS</div>
    <div class="meter" style="top:213px;--pos:49%"></div>
    <div class="metric-name" style="top:252px">SAGITTAL</div><div class="metric-sub" style="top:265px">EXTENSION AT TO</div>
    <div class="meter" style="top:283px;--pos:29%"></div>
    <div class="metric-name" style="top:322px">TRANSVERS</div><div class="metric-sub" style="top:335px">ROTATION INWARDS</div>
    <div class="meter" style="top:353px;--pos:64%"></div>
  </section>

  <section class="panel light" style="left:429px;top:376px;width:181px;height:388px">
    <h2 class="panel-title" style="top:10px">KNEE</h2>
    <div class="artwork" role="img" aria-label="Anatomical model of both lower legs and knees" style="top:36px;width:60px;height:122px"></div>
    <div class="metric-name" style="top:182px">FRONTAL</div><div class="metric-sub" style="top:195px">COLLAPSE IN</div>
    <div class="meter" style="top:213px;--pos:75%"></div>
    <div class="metric-name" style="top:252px">SAGITTAL</div><div class="metric-sub" style="top:265px">BEND AT FOOTSTRIKE</div>
    <div class="meter" style="top:283px;--pos:88%"></div>
    <div class="metric-name" style="top:322px">TRANSVERS</div><div class="metric-sub" style="top:335px">ROTATION INWARDS</div>
    <div class="meter" style="top:353px;--pos:20%"></div>
  </section>

  <section class="panel light" style="left:622px;top:376px;width:181px;height:388px">
    <h2 class="panel-title" style="top:10px">ANKLE</h2>
    <div class="artwork" role="img" aria-label="Anatomical model of the ankle and foot" style="top:50px;width:130px;height:90px"></div>
    <div class="metric-name" style="top:182px">FRONTAL</div><div class="metric-sub" style="top:195px">HEEL COLLAPSE IN</div>
    <div class="meter" style="top:213px;--pos:30%"></div>
    <div class="metric-name" style="top:252px">SAGITTAL</div><div class="metric-sub" style="top:265px">DORSIFLEXION MAX</div>
    <div class="meter" style="top:283px;--pos:45%"></div>
    <div class="metric-name" style="top:322px">TRANSVERS</div><div class="metric-sub" style="top:335px">TIBIA ROTATION INWARDS</div>
    <div class="meter" style="top:353px;--pos:60%"></div>
  </section>

  <!-- Foot strike -->
  <section class="panel" style="left:42px;top:780px;width:374px;height:118px">
    <h2 class="panel-title" style="top:17px">FOOT STRIKE TYPE</h2>
    <span class="label" style="left:21px;top:61px">HEEL</span>
    <span class="label" style="left:160px;top:61px">MIDFOOT</span>
    <span class="label" style="left:300px;top:61px">FOREFOOT</span>
    <div style="position:absolute;left:20px;width:334px;top:83px;height:4px;background:var(--orange)"></div>
    <div class="marker" style="left:66px;top:78px"></div>
  </section>

  <!-- Ground contact -->
  <section class="panel" style="left:429px;top:780px;width:373px;height:118px">
    <h2 class="panel-title" style="top:17px;left:150px;right:0;text-align:left">GROUND CONTACT TIME</h2>
    <div class="big-number" style="left:33px;top:46px;font-size:38px">50</div>
    <div class="unit" style="left:44px;top:78px">SPM</div>
    <span class="label" style="left:106px;top:62px">0</span>
    <span class="label" style="left:225px;top:62px">50</span>
    <span class="label" style="left:337px;top:62px">100</span>
    <div style="position:absolute;left:105px;width:248px;top:83px;height:4px;background:var(--red)"></div>
    <div class="marker" style="left:227px;top:78px"></div>
  </section>

  <!-- Vertical movement -->
  <section class="panel" style="left:42px;top:906px;width:180px;height:246px">
    <h2 class="panel-title" style="top:20px;line-height:17px">VERTICAL<br>MOVEMENT</h2>
    <div style="position:absolute;left:28px;top:76px;width:4px;height:146px;background:linear-gradient(180deg,var(--red),var(--orange) 35%,var(--yellow) 55%,var(--green) 78%,var(--green-dark))"></div>
    <div style="position:absolute;left:23px;top:118px;width:14px;height:5px;background:var(--white)"></div>
    <span class="label" style="left:44px;top:78px">HIGH</span>
    <span class="label" style="left:44px;top:218px">LOW</span>
  </section>

  <!-- Cadence -->
  <section class="panel" style="left:235px;top:906px;width:181px;height:246px">
    <h2 class="panel-title" style="top:22px">CADENCE</h2>
    <div class="big-number" style="left:0;right:0;text-align:center;top:84px;font-size:35px">180</div>
    <div class="unit" style="left:0;right:0;text-align:center;top:116px">SPM</div>
    <svg style="position:absolute;left:15px;top:158px" width="152" height="80" viewBox="0 0 152 80">
      <path d="M2 78 A74 74 0 0 1 17.7 32.3 L76 78 Z" fill="#e89a80"/>
      <path d="M17.7 32.3 A74 74 0 0 1 53.2 7.6 L76 78 Z" fill="#f0c08a"/>
      <path d="M53.2 7.6 A74 74 0 0 1 98.8 7.6 L76 78 Z" fill="#f3e09a"/>
      <path d="M98.8 7.6 A74 74 0 0 1 134.3 32.3 L76 78 Z" fill="#8dbf8f"/>
      <path d="M134.3 32.3 A74 74 0 0 1 150 78 L76 78 Z" fill="#7d8e72"/>
      <path d="M2 78 A74 74 0 0 1 150 78" fill="none" stroke="var(--red)" stroke-width="2"/>
      <path d="M98.8 7.6 A74 74 0 0 1 150 78" fill="none" stroke="var(--green)" stroke-width="2"/>
      <line x1="34" y1="4" x2="76" y2="72" stroke="#6a6f7a" stroke-width="1.5"/>
    </svg>
  </section>

  <!-- Over-stride -->
  <section class="panel" style="left:429px;top:909px;width:373px;height:116px">
    <h2 class="panel-title" style="top:17px">OVER-STRIDE</h2>
    <span class="label" style="left:25px;top:62px">LOW</span>
    <span class="label" style="left:165px;top:62px">MEDIUM</span>
    <span class="label" style="left:343px;top:62px">HI</span>
    <div style="position:absolute;left:25px;width:328px;top:82px;height:4px;background:var(--green)"></div>
    <div class="marker" style="left:227px;top:77px"></div>
  </section>

  <!-- Distance between feet -->
  <section class="panel" style="left:429px;top:1037px;width:373px;height:115px">
    <h2 class="panel-title" style="top:17px">DISTANCE BETWEEN FEET</h2>
    <svg style="position:absolute;left:25px;top:50px" width="328" height="36" viewBox="0 0 328 36">
      <polygon points="0,29 64,24 64,36 0,36" fill="var(--red)"/>
      <polygon points="64,24 135,17 135,36 64,36" fill="var(--orange)"/>
      <polygon points="135,17 205,10 205,36 135,36" fill="var(--yellow)"/>
      <polygon points="205,10 264,4 264,36 205,36" fill="var(--green)"/>
      <polygon points="264,4 328,0 328,36 264,36" fill="var(--green-dark)"/>
    </svg>
    <div class="marker" style="left:227px;top:75px;height:11px"></div>
    <span class="label" style="left:25px;top:92px">NARROW</span>
    <span class="label" style="left:330px;top:92px">WEID</span>
  </section>
</main>
</body>
</html>
```